Broschüre für Gebäudereinigungsservice
Zielgruppe
Wir sind ein Gebäudeservice Unterehmen. Wir sind spezialisiert auf: Reinigungen aller Art, Grünflächenpflege aller Art, Winterdienst und Handwerkerservice aller Art. Usere Zielgruppe: Hausverwaltungen, Genossenschaften und Privatpersonen.
Aufgabenstellung
Die Broschüre soll an diese Kunden per Mail als auch ausgedruckt versendet werden.
Kunden sollen mit dieser Broschüre davon überzeugt werden uns als Gebäudeservice-Unternehmen zu beauftragen.
Unser Firmenslogan lautet 'QUALITÄT DURCH LEISTUNG.'
Die Bilder im Anhang können übernommen werden. Müssen aber nicht, bin für besserer Vorschläge gerne zu haben.
Alle Formate sind erlaubt
Bei Fragen bitte kontaktieren.
Danke!

```html
<!DOCTYPE html>
<html lang="de">
<head>
<meta charset="utf-8">
<title>Kelora Gebäudeservice – Broschüre</title>
<link href="https://fonts.googleapis.com/css2?family=Barlow:wght@300;400;600&family=Barlow+Semi+Condensed:wght@600;700&display=swap" rel="stylesheet">
<style>
  :root{
    --orange:#e8590c;
    --red:#d62d14;
    --text:#3a3a3a;
    --muted:#555;
    --dark:#333;
    --sky-top:#2f86d6;
    --page:#ffffff;
    --canvas:#ffffff;
  }
  *{margin:0;padding:0;box-sizing:border-box}
  html,body{width:748px;height:1200px;overflow:hidden;background:var(--canvas)}
  body{position:relative;font-family:"Barlow",sans-serif;color:var(--text)}
  .spread{position:absolute;left:131px;width:476px;height:504px;background:var(--page);box-shadow:2px 3px 6px rgba(0,0,0,.35);overflow:hidden}
  .spread--cover{top:59px}
  .spread--services{top:623px}
  .spread__art{position:absolute;inset:0}
  .fold{position:absolute;left:237px;top:0;bottom:0;width:1px;background:rgba(0,0,0,.08)}
  .cover-title{position:absolute;left:254px;top:50px;font-family:"Barlow Semi Condensed",sans-serif;font-weight:700;font-size:21px;line-height:19px;color:#fff;letter-spacing:1.2px}
  .intro{position:absolute;left:20px;top:226px;width:200px;font-size:7.2px;line-height:11.3px;font-weight:400;text-align:justify;letter-spacing:.25px}
  .intro__motto{font-family:"Barlow Semi Condensed",sans-serif;font-weight:700;color:var(--orange);font-size:9.5px;letter-spacing:.5px;margin:9px 0 12px}
  .brand-small{position:absolute;left:20px;top:428px;font-family:"Barlow Semi Condensed",sans-serif;font-weight:700;font-size:14px;line-height:13px;color:var(--orange)}
  .brand-small span{display:block;font-size:6px;letter-spacing:.8px;color:var(--dark)}
  .contact{position:absolute;left:20px;top:462px;width:200px;font-size:6px;line-height:9.3px;font-weight:600;display:flex;justify-content:space-between;color:var(--dark)}
  .contact address{font-style:normal}
  .contact dl{display:grid;grid-template-columns:26px auto}
  .contact dt{color:var(--orange)}
  .brand-large{position:absolute;left:266px;top:410px;width:178px;font-family:"Barlow Semi Condensed",sans-serif;font-weight:700;text-align:center}
  .brand-large__name{display:block;font-size:54px;line-height:58px;letter-spacing:1px;color:var(--orange)}
  .brand-large__line{display:block;font-size:14.5px;letter-spacing:2.6px;line-height:18px;color:var(--dark)}
  .service{position:absolute;width:82px}
  .service h3{font-family:"Barlow Semi Condensed",sans-serif;font-weight:700;font-size:7.3px;color:var(--orange);margin-bottom:3px}
  .service ul{list-style:none;font-size:4.3px;line-height:8.5px;color:var(--muted)}
  .service li{padding-left:5px;position:relative}
  .service li::before{content:"";position:absolute;left:0;top:3.3px;width:2px;height:2px;border-radius:50%;background:var(--orange)}
  .s-hand{left:19px;top:271px}
  .s-gruen{left:117px;top:292px;width:76px}
  .s-rein{left:198px;top:320px;width:82px}
  .s-winter{left:291px;top:358px;width:74px}
  .s-entr{left:378px;top:409px;width:80px}
  .services-slogan{position:absolute;left:19px;top:472px;font-family:"Barlow Semi Condensed",sans-serif;font-weight:700;font-size:15px;letter-spacing:.8px;color:var(--orange)}
</style>
</head>
<body>

<section class="spread spread--cover">
  <svg class="spread__art" viewBox="0 0 476 504" width="476" height="504">
    <defs>
      <linearGradient id="sky1" x1="1" y1="0" x2="0" y2="1">
        <stop offset="0" stop-color="var(--sky-top)"/>
        <stop offset=".55" stop-color="#7db8e6"/>
        <stop offset="1" stop-color="#d9e6ee"/>
      </linearGradient>
    </defs>
    <path role="img" aria-label="Foto: modernes Wohnhaus mit Balkonen vor blauem Himmel und Bäumen" d="M0,0H476V365Q260,190 0,155Z" fill="url(#sky1)"/>
    <path d="M0,158Q260,193 476,368" fill="none" stroke="var(--orange)" stroke-width="7"/>
    <path d="M205,210Q390,265 476,385" fill="none" stroke="var(--red)" stroke-width="3.5"/>
    <circle cx="403" cy="290" r="43" fill="#fff"/>
    <circle cx="403" cy="290" r="39" fill="var(--red)"/>
    <text x="403" y="287" text-anchor="middle" font-family="Barlow Semi Condensed, sans-serif" font-weight="700" font-size="11" fill="#fff" letter-spacing=".6">ALLES AUS</text>
    <text x="403" y="300" text-anchor="middle" font-family="Barlow Semi Condensed, sans-serif" font-weight="700" font-size="11" fill="#fff" letter-spacing=".6">EINER HAND</text>
  </svg>
  <div class="fold"></div>
  <h1 class="cover-title">QUALITÄT DURCH<br>LEISTUNG.</h1>
  <div class="intro">
    <p>Wir sind ein seit 2012 bestehendes Familienunternehmen welches nach folgendem Motto lebt:</p>
    <p class="intro__motto">"QUALITÄT DURCH LEISTUNG."</p>
    <p>Dieses Motto hat für uns die höchste Priorität, denn nur wenn sich alle Bewohner wirklich wohl fühlen, haben wir unser Ziel erreicht und unsere Idee verwirklicht. Diese kann nur mit kompetenten Mitarbeitern sowie durch regelmäßige Kontrollen der erbrachten Leistungen sichergestellt werden. Wir sind für unsere Kunden mit unserem Team bekannte Personen, und wir stellen uns immer wieder dem Gespräch mit unseren Kunden. Entscheidungsfreudige Mitarbeiter, die genau erkennen welche Bitten sofort erledigt werden können, oder welche dringend mit uns besprochen werden müssen, helfen die Qualität unserer Leistungen zu gewährleisten.</p>
  </div>
  <div class="brand-small">KELORA<span>GEBÄUDESERVICE</span></div>
  <div class="contact">
    <address>Kelora Gebäudeservice GmbH<br>Lindenhofgasse 12/4<br>1220 Wien</address>
    <dl>
      <dt>Tel:</dt><dd>01/487 22 13</dd>
      <dt>Mail:</dt><dd>office@kelora.at</dd>
      <dt>Web:</dt><dd>www.kelora.at</dd>
    </dl>
  </div>
  <div class="brand-large">
    <span class="brand-large__name">KELORA</span>
    <span class="brand-large__line">GEBÄUDESERVICE</span>
  </div>
</section>

<section class="spread spread--services">
  <svg class="spread__art" viewBox="0 0 476 504" width="476" height="504">
    <defs>
      <linearGradient id="sky2" x1="1" y1="0" x2="0" y2="1">
        <stop offset="0" stop-color="var(--sky-top)"/>
        <stop offset=".55" stop-color="#7db8e6"/>
        <stop offset="1" stop-color="#d9e6ee"/>
      </linearGradient>
    </defs>
    <path role="img" aria-label="Foto: modernes Wohnhaus mit Balkonen vor blauem Himmel und Bäumen" d="M0,0H476V365Q260,190 0,155Z" fill="url(#sky2)"/>
    <path d="M0,158Q260,193 476,368" fill="none" stroke="var(--orange)" stroke-width="7"/>
    <path d="M205,210Q390,265 476,385" fill="none" stroke="var(--red)" stroke-width="3.5"/>
    <circle cx="403" cy="67" r="43" fill="#fff"/>
    <circle cx="403" cy="67" r="39" fill="var(--red)"/>
    <path d="M395,40c2-2 4,1 5,3s-2,3-1,4 3,5 5,6 2-2 4-1 4,3 2,5c-2,2-6,1-10-3s-7-12-5-14z" fill="#fff"/>
    <text x="403" y="74" text-anchor="middle" font-family="Barlow Semi Condensed, sans-serif" font-weight="700" font-size="8" fill="#fff" letter-spacing=".5">24 STUNDEN / 7 TAGE</text>
    <text x="403" y="83" text-anchor="middle" font-family="Barlow Semi Condensed, sans-serif" font-weight="700" font-size="7" fill="#fff" letter-spacing=".5">TELEFON-HOTLINE</text>
    <text x="403" y="96" text-anchor="middle" font-family="Barlow Semi Condensed, sans-serif" font-weight="700" font-size="10" fill="#fff">01/487 22 13</text>
    <circle role="img" aria-label="Foto: Handwerker beim Bohren" cx="59" cy="224" r="35" fill="#b9a48e"/>
    <circle role="img" aria-label="Foto: Rasenmäher auf grünem Rasen" cx="147" cy="244" r="35" fill="#4f9a2e"/>
    <circle role="img" aria-label="Foto: Reinigungskraft mit Putzwagen" cx="237" cy="274" r="35" fill="#dfe3e8"/>
    <circle role="img" aria-label="Foto: Winterdienst beim Schneeräumen" cx="324" cy="311" r="35" fill="#c8d0d8"/>
    <circle role="img" aria-label="Foto: Container mit Sperrmüll" cx="410" cy="369" r="35" fill="#a8927a"/>
  </svg>
  <div class="fold"></div>

  <div class="service s-hand">
    <h3>Handwerker-Service:</h3>
    <ul>
      <li>Reparatur Türen und Fenster</li>
      <li>Kleinflächen verputzen und ausmalen</li>
      <li>Reparatur und Montage Geländer und Handläufe</li>
      <li>Montage Taubennetz u. Taubenspitzen</li>
      <li>Reparatur und Montage Schlösser, Zylinder und Türgriffe</li>
      <li>Reparatur Postkästen</li>
      <li>Reparatur und Montage Gullys &amp; Kanaldeckel</li>
      <li>Reparatur und Montage Türschließer</li>
      <li>Instandsetzung Kaminmauerwerk und Kaminköpfe</li>
      <li>Beseitigung von Stolperfallen</li>
      <li>Montage Lochbleche</li>
      <li>Reparatur Holz-, Keramik- und Terazzoböden</li>
      <li>Montage Kantenschutzprofile</li>
      <li>Befestigung Boden- und Sockelfliesen</li>
      <li>Reparatur gebrochene Betonstufen</li>
      <li>diverse weitere Reparaturarbeiten</li>
    </ul>
  </div>
  <div class="service s-gruen">
    <h3>Grünflächenpflege:</h3>
    <ul>
      <li>Rasenschnitt</li>
      <li>Rasenbewässerung</li>
      <li>Sträucherrückschnitt</li>
      <li>Baumkronenrückschnitt</li>
      <li>Baumrodung</li>
      <li>Baumkronenabwurf</li>
      <li>Wurzelstockfräsung</li>
      <li>Efeubeseitigung</li>
      <li>Düngung</li>
      <li>Fertigrasenverlegung</li>
      <li>Wildkrautbeseitigung</li>
      <li>Laubbeseitigung</li>
      <li>diverse weitere Grünflächenpflegearbeiten</li>
    </ul>
  </div>
  <div class="service s-rein">
    <h3>Reinigung:</h3>
    <ul>
      <li>wöchentliche Stiegenhausreinigung</li>
      <li>Fensterreinigung</li>
      <li>Büroreinigung</li>
      <li>Wohnungsreinigung</li>
      <li>Reinigung Außenflächen</li>
      <li>Garagennassreinigung</li>
      <li>Fassadenreinigung</li>
      <li>Hochdruckreinigung</li>
      <li>Graffitientfernung</li>
      <li>Spezialreinigungen wie Taubenkot</li>
      <li>diverse weitere Reinigungsarbeiten</li>
    </ul>
  </div>
  <div class="service s-winter">
    <h3>Winterdienst:</h3>
    <ul>
      <li>Bereitschaftsdienst vom 01.11. bis 15.04.</li>
      <li>Schneeräumung</li>
      <li>Tauwetterkontrolle</li>
      <li>Splitt- und Salzstreuung</li>
      <li>Splittkehrung bei Trockenperioden</li>
      <li>Montage Dachlawinenstangen</li>
      <li>händische als auch maschinelle Räumung</li>
    </ul>
  </div>
  <div class="service s-entr">
    <h3>Entrümpelung:</h3>
    <ul>
      <li>Fachgerechte Abfallentsorgung</li>
      <li>Sperrmüllentsorgung</li>
      <li>Firmen- und Büroräumungen</li>
      <li>Wohnungsräumungen</li>
      <li>Dachboden- und Kellerräumungen</li>
      <li>diverse weitere Räumungs- und Entrümpelungsarbeiten</li>
    </ul>
  </div>
  <p class="services-slogan">QUALITÄT DURCH LEISTUNG.</p>
</section>

</body>
</html>
```